Lorna Tess Tresses Fancy Business Card’s

I want my business cards to be elite, original and very classy. I want the business cards to match the colors of my logo and to match the design posted. I would love the design of the picture I posted

I want the card all white .
The dripping on the top of the card I want it to match the pink color in my logo that’s also posted .
I need my logo on the business card !
I need my Instagram- @lorna.tess.tresses__
And my phone number - 582 907 3365

Target Market(s)

My target market is young woman age 23 to older woman to the age of 65
I want both older and younger women to love my design . I don’t want any cheap looking business cards

Industry/Entity Type

Hair And Beauty

Contact Information for Business Card

Add my logo
Add my Instagram- @lorna.tess.tresses__
My number - 582 907 3365
My website- www.lornatesstresses.example

Font styles to use
Serif
Script

Colors
ffffff
e667a6
e34298

Requirements
Must have
• The business cards must have my logo, my number , my website, and my Instagram!
Nice to have
• Nice to have glitter words that match my logo
• The business cards must look classy and mature
• I want them to be very unique!!
Should not have
• Should not have any colors that doesn’t match my logo ! This is very important! Please

```html
<!DOCTYPE html>
<html lang="en">
<head>
<meta charset="utf-8">
<title>Lorna Tess Tresses – Business Card</title>
<link rel="stylesheet" href="https://fonts.googleapis.com/css2?family=Kalam:wght@300&display=swap">
<style>
  :root {
    --backdrop: #f6b0c3;
    --card: #ffffff;
    --pink-light: #e667a6;
    --pink-deep: #e34298;
  }
  html, body {
    margin: 0;
    padding: 0;
    width: 1200px;
    height: 1200px;
    overflow: hidden;
    background: var(--backdrop);
  }
  .canvas {
    position: relative;
    width: 1200px;
    height: 1200px;
  }
  .card {
    position: absolute;
    left: 214px;
    width: 763px;
    background: var(--card);
    overflow: hidden;
  }
  .card--back {
    top: 95px;
    height: 424px;
  }
  .card--front {
    top: 607px;
    height: 436px;
  }
  .back-pattern {
    position: absolute;
    inset: 0;
    background:
      repeating-linear-gradient(180deg,
        var(--pink-light) 0 11px, transparent 11px 26px,
        var(--pink-deep) 26px 37px, transparent 37px 52px);
    background-position: 0 6px;
    opacity: 0.85;
  }
  .wave-band {
    position: absolute;
    top: 130px;
    width: 290px;
    height: 120px;
  }
  .wave-band--left { left: 0; }
  .wave-band--right { right: 0; transform: scaleX(-1); }
  .brand {
    position: absolute;
    left: 0;
    right: 0;
    top: 168px;
    display: flex;
    align-items: center;
    justify-content: center;
    gap: 10px;
  }
  .brand__name {
    font-family: "Kalam", cursive;
    font-weight: 300;
    font-size: 30px;
    color: var(--pink-deep);
    line-height: 1;
  }
  .brand__dot {
    width: 22px;
    height: 22px;
    border-radius: 50%;
    background: var(--pink-deep);
  }
  .contacts {
    position: absolute;
    left: 27px;
    right: 20px;
    top: 374px;
    display: flex;
    align-items: center;
  }
  .contact {
    display: flex;
    align-items: center;
    gap: 11px;
    font-family: "Kalam", cursive;
    font-weight: 300;
    font-size: 16px;
    color: var(--pink-deep);
    white-space: nowrap;
  }
  .contact--web { width: 280px; }
  .contact--social { width: 238px; }
  .contact__icon {
    width: 35px;
    height: 35px;
    flex: none;
  }
  .contact__square {
    width: 35px;
    height: 35px;
    border-radius: 8px;
    background: var(--pink-deep);
    flex: none;
  }
</style>
</head>
<body>
<div class="canvas">

  <section class="card card--back">
    <div class="back-pattern" role="img" aria-label="Decorative pattern of rounded pink dashes in alternating rows"></div>
  </section>

  <section class="card card--front">
    <svg class="wave-band wave-band--left" viewBox="0 0 290 120" role="img" aria-label="Decorative flowing bands of pink dashes">
      <defs>
        <linearGradient id="waveFade" x1="0" x2="1" y1="0" y2="0">
          <stop offset="0" stop-color="#e34298"/>
          <stop offset="0.6" stop-color="#e667a6"/>
          <stop offset="1" stop-color="#e667a6" stop-opacity="0.4"/>
        </linearGradient>
      </defs>
      <path d="M0 5 C90 0 130 15 180 35 C220 48 260 45 290 42 L290 112 C250 118 210 118 170 108 C120 95 60 90 0 92 Z" fill="url(#waveFade)"/>
    </svg>
    <svg class="wave-band wave-band--right" viewBox="0 0 290 120" role="img" aria-label="Decorative flowing bands of pink dashes">
      <path d="M0 5 C90 0 130 15 180 35 C220 48 260 45 290 42 L290 112 C250 118 210 118 170 108 C120 95 60 90 0 92 Z" fill="url(#waveFade)"/>
    </svg>

    <div class="brand">
      <span class="brand__name">Lorna Tess Tresses</span>
      <span class="brand__dot"></span>
    </div>

    <div class="contacts">
      <div class="contact contact--web">
        <svg class="contact__icon" viewBox="0 0 36 36" aria-hidden="true">
          <circle cx="18" cy="18" r="17" fill="#e34298"/>
          <g fill="none" stroke="#ffffff" stroke-width="1.6">
            <circle cx="18" cy="18" r="11"/>
            <ellipse cx="18" cy="18" rx="5" ry="11"/>
            <line x1="7" y1="18" x2="29" y2="18"/>
            <line x1="18" y1="7" x2="18" y2="29"/>
            <line x1="9" y1="12.5" x2="27" y2="12.5"/>
            <line x1="9" y1="23.5" x2="27" y2="23.5"/>
          </g>
        </svg>
        <span>www.lornatesstresses.example</span>
      </div>
      <div class="contact contact--social">
        <span class="contact__square"></span>
        <span>@lorna.tess.tresses__</span>
      </div>
      <div class="contact contact--phone">
        <svg class="contact__icon" viewBox="0 0 36 36" aria-hidden="true">
          <circle cx="18" cy="18" r="17" fill="#e34298"/>
          <circle cx="18" cy="14" r="4.5" fill="#ffffff"/>
          <path d="M10.5 26 C10.5 20.5 25.5 20.5 25.5 26 Z" fill="#ffffff"/>
        </svg>
        <span>582 907 3365</span>
      </div>
    </div>
  </section>

</div>
</body>
</html>
```